Corrindale Planners, LLC Stationary

Corrindale Planners, LLC is a new financial planning and consulting company. We are looking for designs on business cards, letterhead, envelopes, and anything else that would be useful. Our preference for business card design is two sided. We are looking for a professional and clean look with incorporating the logo and patriotic feel. Thank you to all who participate and good luck!

```html
<!DOCTYPE html>
<html lang="en">
<head>
<meta charset="utf-8">
<title>Corrindale Planners, LLC — Stationery</title>
<link rel="stylesheet" href="https://fonts.googleapis.com/css2?family=Open+Sans:wght@400;600&family=Libre+Baskerville&display=swap">
<style>
  :root {
    --navy: #0f3c68;
    --navy-deep: #0c3259;
    --red: #c8202b;
    --paper: #ffffff;
    --ink: #3a3a3a;
    --muted: #6b6b6b;
    --backdrop: #cfe3ea;
  }
  * { box-sizing: border-box; margin: 0; padding: 0; }
  html, body { width: 1200px; height: 1073px; overflow: hidden; }
  body {
    background: var(--backdrop);
    font-family: "Open Sans", sans-serif;
    position: relative;
  }
  .piece { position: absolute; background: var(--paper); box-shadow: 0 2px 6px rgba(0,0,0,.12); overflow: hidden; }
  .piece svg.art { position: absolute; left: 0; top: 0; width: 100%; height: 100%; }
  .brand-name { font-family: "Open Sans", sans-serif; font-weight: 600; color: var(--navy); white-space: nowrap; }

  /* folder */
  .folder { left: 175px; top: 121px; width: 415px; height: 563px; background: var(--navy-deep); }

  /* letterhead */
  .letterhead { left: 112px; top: 68px; width: 415px; height: 563px; }
  .letterhead .header-name { position: absolute; top: 40px; left: 0; width: 100%; text-align: center; font-size: 13px; }
  .letterhead .title { position: absolute; top: 168px; width: 100%; text-align: center; font-size: 16px; font-weight: 400; color: var(--ink); letter-spacing: .5px; }
  .letterhead .body { position: absolute; top: 210px; left: 54px; width: 308px; font-size: 6.4px; line-height: 11.2px; color: var(--muted); text-align: justify; }
  .letterhead .signature { position: absolute; top: 348px; left: 292px; width: 62px; height: 18px; background: linear-gradient(90deg, #eeeeee, #dcdcdc); border-radius: 3px; }
  .letterhead .signer { position: absolute; top: 373px; right: 55px; font-size: 4.6px; color: var(--ink); }
  .letterhead .foot-name { position: absolute; right: 12px; bottom: 10px; font-size: 7px; }

  /* business cards */
  .card { width: 175px; height: 100px; }
  .card-front { left: 844px; top: 405px; background: linear-gradient(135deg, #f4f5f7 0%, #e8ebef 100%); }
  .card-front .brand-name { position: absolute; top: 44px; width: 100%; text-align: center; font-size: 11px; }
  .card-back { left: 843px; top: 549px; }
  .card-back .person { position: absolute; top: 15px; left: 52px; width: 120px; text-align: center; font-family: "Libre Baskerville", serif; font-size: 10px; color: var(--navy); }
  .card-back .person .last { color: var(--red); }
  .card-back .role { position: absolute; top: 29px; left: 52px; width: 120px; text-align: center; font-size: 6px; color: var(--navy); }
  .card-back .contacts { position: absolute; top: 53px; left: 9px; list-style: none; }
  .card-back .contacts li { display: flex; align-items: center; gap: 4px; height: 10px; font-size: 4.4px; color: #fff; }
  .card-back .contacts svg { width: 6px; height: 6px; }
  .card-back .foot-name { position: absolute; right: 6px; bottom: 8px; font-size: 5px; }

  /* envelope back */
  .envelope-back { left: 562px; top: 725px; width: 408px; height: 286px; background: transparent; box-shadow: none; }
  .envelope-back .phone { position: absolute; top: 32px; left: 180px; font-size: 9px; color: rgba(255,255,255,.85); }
  .envelope-back .return { position: absolute; left: 290px; top: 238px; width: 96px; font-size: 4.6px; line-height: 6.6px; color: var(--ink); }
  .envelope-back .return-name { position: absolute; left: 200px; top: 242px; font-size: 6px; }

  /* envelope front */
  .envelope-front { left: 364px; top: 777px; width: 409px; height: 191px; }
  .envelope-front .foot-name { position: absolute; right: 26px; bottom: 30px; font-size: 7px; }
</style>
</head>
<body>

  <div class="piece folder" aria-hidden="true"></div>

  <section class="piece letterhead">
    <svg class="art" viewBox="0 0 415 563" aria-hidden="true">
      <polygon points="0,455 309,526 0,459" fill="var(--navy)"/>
      <polygon points="0,465 309,530 196,563 0,563" fill="var(--navy)"/>
      <polygon points="196,563 415,493 415,499 222,563" fill="var(--red)"/>
    </svg>
    <p class="brand-name header-name">Corrindale Planners, LLC</p>
    <h1 class="title">OUR MISSION</h1>
    <p class="body">Lorem ipsum dolor sit amet, consectetur adipiscing elit. Donec orci purus, luctus vitae dignissim eu, iaculis sed purus. Vivamus faucibus, ipsum nec aliquet viverra, leo mauris condimentum ligula, sit amet sagittis enim ligula quis arcu. Nam egestas tortor id nisi porttitor mattis. In tortor ante, ultricies in suscipit a, tempus non massa. Vivamus et auctor mi. Fusce vel massa nulla. Phasellus nec eros mauris, et scelerisque orci. Donec malesuada orci vitae nulla accumsan porta a id massa. Quisque accumsan iaculis magna sit amet fringilla. Maecenas consequat, magna eget tincidunt semper, odio nibh rutrum mi, id feugiat ante nisi eu risus. Vestibulum nunc orci, rhoncus a placerat in, ultricies in mi. Cras mattis varius eros, vel fringilla nisi suscipit eget.</p>
    <div class="signature" role="img" aria-label="Handwritten signature of Clara Voss"></div>
    <p class="signer">Clara Voss, Co-Founder &amp; CEO</p>
    <p class="brand-name foot-name">Corrindale Planners, LLC</p>
  </section>

  <section class="piece card card-front">
    <svg class="art" viewBox="0 0 175 100" aria-hidden="true">
      <polygon points="82,100 175,70 175,74 92,100" fill="#f3d5d7"/>
    </svg>
    <p class="brand-name">Corrindale Planners, LLC</p>
  </section>

  <section class="piece card card-back">
    <svg class="art" viewBox="0 0 175 100" aria-hidden="true">
      <polygon points="0,15 132,66 0,17" fill="var(--navy)"/>
      <polygon points="0,20 130,70 84,100 0,100" fill="var(--navy)"/>
      <polygon points="84,100 175,46 175,50 92,100" fill="var(--red)"/>
    </svg>
    <p class="person">DANIEL <span class="last">REYES</span></p>
    <p class="role">FINANCIAL PLANNER</p>
    <ul class="contacts">
      <li><svg viewBox="0 0 10 10"><circle cx="5" cy="5" r="4.5" fill="none" stroke="#fff"/><path d="M2.8 5.4 5 3.2 7.2 5.4V7.2H2.8Z" fill="#fff"/></svg>Address</li>
      <li><svg viewBox="0 0 10 10"><circle cx="5" cy="5" r="4.5" fill="none" stroke="#fff"/><rect x="2.6" y="3.4" width="4.8" height="3.4" fill="#fff"/></svg>daniel.reyes@corrindaleplanners.com</li>
      <li><svg viewBox="0 0 10 10"><circle cx="5" cy="5" r="4.5" fill="none" stroke="#fff"/><path d="M3.3 2.8 4.3 4.3 3.8 4.9Q4.6 6 5.6 6.4L6.1 5.8 7.3 6.8 6.6 7.4Q4.2 7 3 4Z" fill="#fff"/></svg>(555) 555-0182</li>
      <li><svg viewBox="0 0 10 10"><circle cx="5" cy="5" r="4.5" fill="none" stroke="#fff"/><circle cx="5" cy="5" r="2.4" fill="none" stroke="#fff" stroke-width=".8"/></svg>www.corrindaleplanners.com</li>
    </ul>
    <p class="brand-name foot-name">Corrindale</p>
  </section>

  <section class="piece envelope-back">
    <svg class="art" viewBox="0 0 408 286" aria-hidden="true">
      <path d="M22 0H368Q378 0 380 12L408 100V286H14V100L10 12Q12 0 22 0Z" fill="var(--navy)"/>
      <rect x="14" y="100" width="394" height="186" fill="var(--paper)"/>
      <polygon points="14,100 200,285 14,285" fill="#f4f4f4"/>
      <polygon points="408,100 250,100 200,285 408,285" fill="#fafafa"/>
      <polygon points="380,100 408,100 390,176" fill="var(--navy-deep)"/>
    </svg>
    <p class="phone">(555) 555-0182</p>
    <p class="brand-name return-name">Corrindale</p>
    <p class="return">Planning for every stage of life, with clear advice and steady guidance from our team.</p>
  </section>

  <section class="piece envelope-front">
    <svg class="art" viewBox="0 0 409 191" aria-hidden="true">
      <polygon points="0,6 305,122 0,11" fill="var(--navy)"/>
      <polygon points="0,16 304,129 190,191 0,191" fill="var(--navy)"/>
      <polygon points="190,191 409,66 409,73 212,191" fill="var(--red)"/>
    </svg>
    <p class="brand-name foot-name">Corrindale Planners, LLC</p>
  </section>

</body>
</html>
```